Modern & Fresh Sumeray Book Cover

Need a creative e-book cover for my book.

Title: Get Sumeray Sorted
Subtitle: Learn How To Easily Choose & Enroll in the Perfect Coverage at the Perfect Time.

Target Market(s)

60-70 year olds in the United States

Font styles to use
Sans Serif

Colors
9bcb3c
33a6d7

Requirements
Must have
• Must look modern and fresh.
• Use our company colors www.BrovaMint.com

```html
<!DOCTYPE html>
<html lang="en">
<head>
<meta charset="utf-8">
<title>Get Sumeray Sorted – Book Cover</title>
<link href="https://fonts.googleapis.com/css2?family=Bebas+Neue&display=swap" rel="stylesheet">
<style>
  :root {
    --sky-top: #2581c0;
    --sky-mid: #36a9dc;
    --sky-bottom: #2d96cf;
    --brand-blue: #33a6d7;
    --brand-green: #9bcb3c;
    --frame-cyan: #6cc9e8;
    --ink-navy: #173a73;
    --paper: #ffffff;
  }
  html, body { margin: 0; padding: 0; overflow: hidden; background: #ffffff; }
  .cover {
    position: relative;
    width: 800px;
    height: 1200px;
    overflow: hidden;
    font-family: "Bebas Neue", "Arial Narrow", sans-serif;
  }
  .cover-art { position: absolute; inset: 0; display: block; }
  .author, .title-small, .title-mid, .title-big { fill: var(--paper); }
  .tagline { fill: var(--ink-navy); }
  .title-rule { stroke: var(--paper); stroke-width: 3; }
  .photo-hex { stroke: var(--frame-cyan); stroke-width: 4; }
</style>
</head>
<body>
<main class="cover">
  <svg class="cover-art" width="800" height="1200" viewBox="0 0 800 1200" xmlns="http://www.w3.org/2000/svg">
    <defs>
      <linearGradient id="skyGrad" x1="0" y1="0" x2="0" y2="1">
        <stop offset="0" stop-color="var(--sky-top)"/>
        <stop offset="0.4" stop-color="var(--sky-mid)"/>
        <stop offset="1" stop-color="var(--sky-bottom)"/>
      </linearGradient>
      <radialGradient id="backdropGlow" cx="0.5" cy="0.55" r="0.6">
        <stop offset="0" stop-color="#5bbfe4" stop-opacity="0.55"/>
        <stop offset="1" stop-color="#5bbfe4" stop-opacity="0"/>
      </radialGradient>
      <polygon id="hex" points="108.8,0 54.4,94.2 -54.4,94.2 -108.8,0 -54.4,-94.2 54.4,-94.2"/>
      <linearGradient id="photoWarm" x1="0" y1="0" x2="1" y2="1">
        <stop offset="0" stop-color="#d9d3d6"/><stop offset="1" stop-color="#b9a39a"/>
      </linearGradient>
      <linearGradient id="photoSky" x1="0" y1="0" x2="0" y2="1">
        <stop offset="0" stop-color="#9fd6f2"/><stop offset="0.75" stop-color="#7fb2c9"/><stop offset="1" stop-color="#4f9a3a"/>
      </linearGradient>
      <linearGradient id="photoSunset" x1="0" y1="0" x2="1" y2="0">
        <stop offset="0" stop-color="#5d4636"/><stop offset="0.7" stop-color="#a87a5c"/><stop offset="1" stop-color="#e9b27a"/>
      </linearGradient>
      <linearGradient id="photoPink" x1="0" y1="0" x2="1" y2="1">
        <stop offset="0" stop-color="#cdb7c2"/><stop offset="1" stop-color="#8f7a86"/>
      </linearGradient>
      <linearGradient id="photoWall" x1="0" y1="0" x2="0" y2="1">
        <stop offset="0" stop-color="#e6ddd2"/><stop offset="1" stop-color="#8aa1b8"/>
      </linearGradient>
      <linearGradient id="photoLilac" x1="0" y1="0" x2="1" y2="1">
        <stop offset="0" stop-color="#b2968a"/><stop offset="1" stop-color="#d9b4d8"/>
      </linearGradient>
    </defs>

    <rect class="background" width="800" height="1200" fill="url(#skyGrad)"/>
    <rect class="backdrop-glow" x="0" y="460" width="800" height="622" fill="url(#backdropGlow)"
          role="img" aria-label="Soft blue backdrop behind the photo tiles"/>

    <text class="author" x="392" y="52" text-anchor="middle" font-size="26" textLength="632" lengthAdjust="spacing">AUTHOR NAME</text>

    <line class="title-rule" x1="32" y1="130" x2="308" y2="130"/>
    <line class="title-rule" x1="490" y1="130" x2="766" y2="130"/>
    <text class="title-small" x="404" y="137" text-anchor="middle" font-size="52">GET</text>
    <text class="title-mid" x="52" y="256" font-size="136" textLength="704" lengthAdjust="spacing">SUMERAY</text>
    <text class="title-big" x="48" y="448" font-size="240" textLength="716" lengthAdjust="spacing">SORTED</text>

    <g class="photos">
      <use href="#hex" class="photo-hex" x="248" y="582" fill="url(#photoWarm)" role="img" aria-label="Photo of a smiling older couple relaxing together"/>
      <use href="#hex" class="photo-hex" x="411.2" y="677" fill="url(#photoSky)" role="img" aria-label="Photo of an older couple riding bicycles under a blue sky"/>
      <use href="#hex" class="photo-hex" x="248" y="771" fill="url(#photoSunset)" role="img" aria-label="Photo of an older man in a beanie smiling at sunset"/>
      <use href="#hex" class="photo-hex" x="574.4" y="771" fill="url(#photoPink)" role="img" aria-label="Photo of a happy older couple posing together"/>
      <use href="#hex" class="photo-hex" x="411.2" y="866" fill="url(#photoWall)" role="img" aria-label="Photo of an older man in a flat cap smiling"/>
      <use href="#hex" class="photo-hex" x="574.4" y="960" fill="url(#photoLilac)" role="img" aria-label="Photo of an older woman laughing beside flowers"/>
    </g>

    <rect class="tagline-band" x="0" y="1082" width="800" height="118" fill="var(--brand-green)"/>
    <text class="tagline" x="92" y="1132" font-size="30" textLength="632" lengthAdjust="spacing">LEARN HOW TO EASILY CHOOSE &amp; ENROLL</text>
    <text class="tagline" x="16" y="1168" font-size="30" textLength="776" lengthAdjust="spacing">IN THE PERFECT COVERAGE AT THE PERFECT TIME.</text>
  </svg>
</main>
</body>
</html>
```